Velvet Glow Co. Derma Roller packaging design

I need a box designed for a skin care brand called Velvet Glow Co. The box will be for our Derma Roller- a skin rejuvenation device. It will be sold online with lots of competition. I would like a modern, high end design, something that stands out and looks amazing. My logo is blush pink and black, for packaging i need no more than 3 colours, maybe gold if any other colour is used. A photo of a sample derma roller is attached below for an idea of what the product looks like, however my roller with have a clear handle with a black roller. The roller comes in a clear case, the box dimensions will need to be 16 cm long, 4 cm high, 4.5 cm wide.
ATTACHED ARE 2 SAMPLE BOXES AS AN EXAMPLE OF THE SIZE OF BOX REQUIRED!

Target Market(s)

25-50 year old women in the US

Colors
e667a6
000000
efefef

Requirements
Must have
• LOGO
• NAME OF PRODUCT- Cosmetic Derma Roller
• NEEDLE DEPTH- 0.25mm
• CAUTION- For personal use only, Do not use if allergic to metal, Do not use on open skin, wounds or active acne, sterilise roller before and after use.
Nice to have
• BENEFITS- Skin Rejuvenation, Collagen Induction Therapy, Increase product absorption, reduce acne scars and pigmentation
• FEATURES- 540 high quality titanium needles, ultra sharp needle tips, cross-line needle arrangement, ergonomic handle, anti slip grip,

```html
<!DOCTYPE html>
<html lang="en">
<head>
<meta charset="utf-8">
<title>Velvet Glow Co. – Cosmetic Derma Roller Packaging</title>
<link rel="stylesheet" href="https://fonts.googleapis.com/css2?family=Oswald:wght@400;500&display=swap">
<style>
  :root {
    --backdrop: #f8f3f1;
    --blush: #f1d9d6;
    --blush-light: #f7e9e7;
    --marble-vein: #b9aaa9;
    --cream: #fdf8f5;
    --rose-gold: #c98f78;
    --rose-gold-light: #e6c1b0;
    --ink: #151112;
  }
  * { margin: 0; padding: 0; box-sizing: border-box; }
  html, body { width: 1200px; height: 1200px; overflow: hidden; }
  body {
    background: radial-gradient(ellipse at center, #fdfbfa 0%, var(--backdrop) 100%);
    font-family: "Oswald", "Arial Narrow", sans-serif;
    position: relative;
  }
  .box-panel {
    position: absolute;
    left: 48px;
    width: 1104px;
    height: 356px;
    box-shadow: 0 6px 14px rgba(60, 40, 40, 0.35);
    overflow: hidden;
  }
  .box-panel--front { top: 182px; }
  .box-panel--back { top: 662px; }
  .marble-surface {
    position: absolute;
    inset: 0;
    background:
      radial-gradient(ellipse 30% 40% at 20% 30%, rgba(185,170,169,0.45), transparent 70%),
      radial-gradient(ellipse 25% 35% at 80% 70%, rgba(185,170,169,0.4), transparent 70%),
      radial-gradient(ellipse 40% 30% at 60% 20%, rgba(255,255,255,0.5), transparent 70%),
      linear-gradient(135deg, var(--blush-light) 0%, var(--blush) 50%, var(--blush-light) 100%);
  }
  .label-card {
    position: absolute;
    background: var(--cream);
    text-align: center;
  }
  .label-card--front {
    left: 386px;
    top: 40px;
    width: 332px;
    height: 280px;
    border: 3px solid var(--rose-gold);
  }
  .label-card--back {
    left: 248px;
    top: 58px;
    width: 608px;
    height: 238px;
  }
  .brand-name {
    position: absolute;
    left: 0; right: 0;
    top: 92px;
    font-size: 34px;
    font-weight: 400;
    letter-spacing: 3px;
    color: var(--ink);
    text-transform: uppercase;
  }
  .product-title {
    font-size: 30px;
    font-weight: 400;
    letter-spacing: 0.5px;
    color: var(--rose-gold);
    background: linear-gradient(90deg, var(--rose-gold-light), var(--rose-gold) 60%, #b77a63);
    -webkit-background-clip: text;
    background-clip: text;
    -webkit-text-fill-color: transparent;
    text-transform: uppercase;
  }
  .label-card--front .product-title {
    position: absolute;
    left: 0; right: 0;
    top: 218px;
  }
  .label-card--back .product-title { margin-top: 22px; }
  .product-details {
    text-align: left;
    padding: 8px 28px 0 29px;
    color: var(--ink);
    font-size: 13.5px;
    line-height: 18px;
    text-transform: uppercase;
  }
  .product-details p + p { margin-top: 18px; }
</style>
</head>
<body>
  <section class="box-panel box-panel--front">
    <div class="marble-surface" role="img" aria-label="Blush pink marble texture with grey veining"></div>
    <div class="label-card label-card--front">
      <div class="brand-name">Velvet Glow Co.</div>
      <h1 class="product-title">Cosmetic Derma Roller</h1>
    </div>
  </section>

  <section class="box-panel box-panel--back">
    <div class="marble-surface" role="img" aria-label="Blush pink marble texture with grey veining"></div>
    <div class="label-card label-card--back">
      <h2 class="product-title">Cosmetic Derma Roller</h2>
      <div class="product-details">
        <p>Benefits: skin rejuvenation, collagen induction therapy, increase product absorption, reduce acne scars and pigmentation</p>
        <p>Features: 540 high quality 0.25 mm titanium needles, ultra sharp needle tips, cross-line needle arrangement, ergonomic handle, anti slip grip</p>
        <p>Caution: for personal use only, do not use if allergic to metal, do not use on open skin, wounds or active acne, sterilise roller before and after use.</p>
      </div>
    </div>
  </section>
</body>
</html>
```